Velvet Brook is looking for packaging design

We need packaging designs for 5 lines.
Velvet Bloom (pink) - incorporates flowers such as rose, hibiscus, rooibos and fireweed.
Velvet Balance (green) - green tea, comfrey, calendula, dandelion, etc.
Velvet Slumber (lavender) - lavender, violet leaf, orris root, rosemary, chamomile, etc.
Velvet Stillness (blue) - cornflower, seaweed, kelp, etc.
Velvet Star Maiden (white) - white tea, marshmallow, elderflowers, jasmine, etc.

A design is needed for each color so that it can be used for labels on jars and bottles as well as for product boxes. It would be great to see the actual type of flower that is used in the product, incorporated into the design. Additionally, labels will need to be created for the facial steams - Herbal Lumina for mature skin, dry skin, oily skin, and acneic.

We are looking for designs that use flowers, herbs and have a very feminine and expensive feel to it. Preferably an illustration or graphic design versus a photographic print.

It would be a bonus if a tiny fairy could be incorporated into the design somewhere in the picture (not one that stands out but small one that blends in with the background) as well as a crystal (ie. like a little diamond). The logo will be on a black background and the jars/bottles will all be black (examples of the bottle colors have been included as well as the clear glass one for facial steams & bath salts).

Target Market(s)

Sold to high end spas.

Current soap packaging has been attached. I am wondering if someone is able to design a background image that is similar but incorporates the flowers/herbs that are put into the product as well as hiding a tiny fairy and crystal.

Industry/Entity Type

Graphic Design

Requirements
Must have
• 5 product labels or box designs. Flowers and herbs in the graphic design.
A crystal placed somewhere within the background.
A tiny fairy placed somewhere within the background that blends in with the picture. ie. could just be the outline of a fairy or it could be the same color as the background.
Nice to have
• A herbal/flower background for steams.

```html
<!DOCTYPE html>
<html lang="en">
<head>
<meta charset="utf-8">
<title>Velvet Brook — Label Designs</title>
<link rel="stylesheet" href="https://fonts.googleapis.com/css2?family=Cinzel:wght@500&family=Lobster&display=swap">
<style>
  :root {
    --page-bg: #ffffff;
    --label-black: #050505;
    --ring-bloom: #f01fd0;
    --ring-balance: #12b83a;
    --brand-white: #f4f1ec;
    --brand-gold: #c9953a;
    --title-tint: rgba(225, 222, 226, 0.72);
    --bloom-rose: #8a4a63;
    --bloom-deep: #4a2133;
    --balance-leaf: #4f6e2c;
    --balance-deep: #22331a;
    --balance-petal: #c7761f;
  }
  * { margin: 0; padding: 0; box-sizing: border-box; }
  html, body {
    width: 1200px;
    height: 846px;
    overflow: hidden;
    background: var(--page-bg);
  }
  .label-sheet {
    position: relative;
    width: 1200px;
    height: 846px;
  }
  .label {
    position: absolute;
    top: 131px;
    width: 544px;
    height: 544px;
    border-radius: 50%;
    border: 6px solid var(--ring-color);
    background: var(--page-bg);
    padding: 9px;
  }
  .label--bloom { left: 49px; --ring-color: var(--ring-bloom); }
  .label--balance { left: 620px; --ring-color: var(--ring-balance); }

  .label__face {
    position: relative;
    width: 100%;
    height: 100%;
    border-radius: 50%;
    overflow: hidden;
    background: var(--label-black);
  }
  .label__botanicals {
    position: absolute;
    inset: 0;
    border-radius: 50%;
  }
  .label--bloom .label__botanicals {
    background:
      radial-gradient(circle at 28% 30%, var(--bloom-rose) 0%, transparent 32%),
      radial-gradient(circle at 70% 38%, var(--bloom-rose) 0%, transparent 30%),
      radial-gradient(circle at 60% 75%, var(--bloom-rose) 0%, transparent 34%),
      radial-gradient(circle at 22% 70%, var(--bloom-deep) 0%, transparent 34%),
      radial-gradient(circle at 50% 50%, var(--bloom-deep) 0%, var(--label-black) 78%);
  }
  .label--balance .label__botanicals {
    background:
      radial-gradient(circle at 62% 38%, var(--balance-petal) 0%, transparent 16%),
      radial-gradient(circle at 76% 66%, var(--balance-petal) 0%, transparent 18%),
      radial-gradient(circle at 38% 68%, var(--balance-petal) 0%, transparent 12%),
      radial-gradient(ellipse at 52% 52%, var(--balance-leaf) 0%, var(--balance-deep) 48%, var(--label-black) 72%);
  }

  .label__brand {
    position: absolute;
    top: 58px;
    left: 0;
    right: 0;
    display: flex;
    flex-direction: column;
    align-items: center;
    gap: 12px;
  }
  .brand__dot {
    width: 26px;
    height: 26px;
    border-radius: 50%;
    background: var(--brand-gold);
  }
  .brand__name {
    font-family: "Cinzel", "Times New Roman", serif;
    font-weight: 500;
    font-size: 25px;
    letter-spacing: 0.5px;
    color: var(--brand-white);
  }

  .label__title {
    position: absolute;
    top: 50%;
    left: 0;
    right: 0;
    transform: translateY(-62%);
    text-align: center;
    font-family: "Lobster", "Brush Script MT", cursive;
    font-size: 80px;
    line-height: 1;
    color: var(--title-tint);
    white-space: nowrap;
  }
  .label--balance .label__title { font-size: 70px; }
</style>
</head>
<body>
  <main class="label-sheet">
    <section class="label label--bloom">
      <div class="label__face">
        <div class="label__botanicals" role="img" aria-label="Pink roses, hibiscus and petunias with rosemary sprigs and a tiny fairy silhouette on black"></div>
        <div class="label__brand">
          <span class="brand__dot"></span>
          <span class="brand__name">Velvet Brook</span>
        </div>
        <h2 class="label__title">Velvet Bloom</h2>
      </div>
    </section>

    <section class="label label--balance">
      <div class="label__face">
        <div class="label__botanicals" role="img" aria-label="Green comfrey leaves, orange calendula, yellow and seeded dandelions, a violet bloom and a tiny fairy silhouette on black"></div>
        <div class="label__brand">
          <span class="brand__dot"></span>
          <span class="brand__name">Velvet Brook</span>
        </div>
        <h2 class="label__title">Velvet Balance</h2>
      </div>
    </section>
  </main>
</body>
</html>
```